Redesign Login page

I want to redesign my login page to bring my 2 products closer together. I am only looking to redesign one login page, not 2.

For the logo, please make it solid and it can be black or white if helpful. I can also fine tune the logo if you get it close.

Coding

Coded - Design and coding required

Number of Pages Required

1 page

```html
<!DOCTYPE html>
<html lang="en">
<head>
<meta charset="UTF-8">
<title>Kelvale – Sign in</title>
<link href="https://fonts.googleapis.com/css2?family=Nunito+Sans:wght@400;600;700;800&display=swap" rel="stylesheet">
<style>
  :root {
    --bg: #03302c;
    --card: #ffffff;
    --field: #e8effc;
    --ink: #2f5a52;
    --ink-dark: #0b2f2a;
    --button: #44655f;
    --line: #dfe5e3;
  }
  * { box-sizing: border-box; margin: 0; padding: 0; }
  html, body {
    width: 1200px; height: 562px; overflow: hidden;
    background: var(--bg);
    font-family: "Nunito Sans", sans-serif;
    color: var(--ink);
  }
  .login-card {
    position: absolute; left: 415px; top: 64px;
    width: 370px; height: 399px;
    background: var(--card); border-radius: 12px;
  }
  .welcome {
    position: absolute; top: 24px; width: 100%;
    text-align: center; font-size: 10px; font-weight: 700;
  }
  .brand {
    position: absolute; top: 50px; width: 100%;
    display: flex; justify-content: center; align-items: center; gap: 8px;
    font-size: 30px; font-weight: 800; color: var(--ink-dark); letter-spacing: -0.5px;
  }
  .brand-mark { width: 18px; height: 18px; background: var(--ink-dark); border-radius: 50%; }
  .field {
    position: absolute; left: 31px; width: 308px; height: 34px;
    background: var(--field); border-radius: 17px;
    display: flex; align-items: center; gap: 8px; padding-left: 15px;
    font-size: 8.5px; font-weight: 600;
  }
  .field svg { width: 11px; height: 11px; fill: var(--ink); }
  .field-email { top: 120px; }
  .field-password { top: 164px; }
  .options {
    position: absolute; left: 31px; top: 210px; width: 308px;
    display: flex; justify-content: space-between; align-items: center;
    font-size: 9.5px; color: #1d1d1d;
  }
  .remember { display: flex; align-items: center; gap: 7px; }
  .checkbox { width: 12px; height: 12px; border: 1px solid #555; border-radius: 2px; }
  .sign-in {
    position: absolute; left: 31px; top: 233px; width: 308px; height: 34px;
    background: var(--button); border-radius: 17px; color: #fff;
    display: flex; align-items: center; justify-content: center;
    font-size: 10px; font-weight: 700;
  }
  .signup {
    position: absolute; top: 288px; width: 100%; text-align: center; font-size: 9.5px;
  }
  .signup strong { font-weight: 700; }
  .divider {
    position: absolute; top: 315px; width: 100%; text-align: center;
    font-size: 9.5px; font-weight: 700;
  }
  .sso {
    position: absolute; top: 340px; width: 150px; height: 34px;
    border: 1px solid var(--line); border-radius: 17px;
    box-shadow: 0 1px 3px rgba(0,0,0,0.12);
    display: flex; align-items: center; justify-content: center; gap: 7px;
    font-size: 8.5px; font-weight: 600;
  }
  .sso-orbit { left: 31px; }
  .sso-tessel { left: 189px; }
  .sso-dot { width: 11px; height: 11px; background: var(--ink); border-radius: 50%; }
  .sso-square { width: 11px; height: 11px; background: var(--ink); }
</style>
</head>
<body>
  <main class="login-card">
    <p class="welcome">Welcome to</p>
    <div class="brand"><span class="brand-mark"></span>Kelvale</div>

    <div class="field field-email">
      <svg viewBox="0 0 16 16"><path d="M1 3h14v10H1z M1 3l7 5 7-5" fill="var(--ink)"/><path d="M1.5 3.5L8 8l6.5-4.5" stroke="#e8effc" stroke-width="1.4" fill="none"/></svg>
      Email Address
    </div>
    <div class="field field-password">
      <svg viewBox="0 0 16 16"><rect x="4" y="7" width="8" height="6" rx="1"/><path d="M5.5 7V5a2.5 2.5 0 0 1 5 0v2" stroke="var(--ink)" stroke-width="1.5" fill="none"/></svg>
      Password
    </div>

    <div class="options">
      <label class="remember"><span class="checkbox"></span>Remember me</label>
      <span>Forgot Password</span>
    </div>

    <div class="sign-in">SIGN IN</div>

    <p class="signup">Don’t have an account? <strong>Sign up</strong></p>
    <p class="divider">OR</p>

    <div class="sso sso-orbit"><span class="sso-dot"></span>Orbit SSO</div>
    <div class="sso sso-tessel"><span class="sso-square"></span>Tessel SSO</div>
  </main>
</body>
</html>
```